Uprising SaaS company needs an attractive business card design

We're an uprising SaaS company who's attempting to attack the rigid car (insurance) claims management market in Europe.
We want to our mighty base order management system, listen to our clients to connect the smart ideas to build something even mightier.
We primarily focus on helping our customers manage their customers' claims/orders and get them resolved as smoothly as possible.
We'd like the business card design to express technical innovation and the fact that we connect smart ideas, as our company slogan indicates.
Contact Information for Business Card
Name, position, website, email, mobile, business address
Font styles to use
Colors
Designer to choose colors to be used in the design.
Look and feel
Each slider illustrates characteristics of the customer's brand and the style your logo design should communicate.

```html
<!DOCTYPE html>
<html lang="en">
<head>
<meta charset="utf-8">
<title>veltrano — business card</title>
<link rel="stylesheet" href="https://fonts.googleapis.com/css2?family=Montserrat:wght@400;500;700&display=swap">
<style>
  :root {
    --backdrop: #b3b3b3;
    --card-front: #7f7f7f;
    --front-mark: #c9c9c9;
    --card-back: #ffffff;
    --brand-gray: #767676;
    --brand-blue: #7ccbe2;
    --ink: #1e1e1e;
  }
  * { margin: 0; padding: 0; box-sizing: border-box; }
  html, body { width: 1200px; height: 900px; overflow: hidden; }
  body {
    background: var(--backdrop);
    font-family: "Montserrat", sans-serif;
    position: relative;
  }
  .card {
    position: absolute;
    left: 320px;
    width: 560px;
    height: 340px;
    border-radius: 22px;
    box-shadow: 0 6px 18px rgba(0,0,0,0.18);
    overflow: hidden;
  }
  .card--front { top: 70px; background: var(--card-front); display: flex; align-items: center; justify-content: center; }
  .card--back { top: 470px; background: var(--card-back); }

  .wordmark {
    font-weight: 400;
    letter-spacing: 2px;
    line-height: 1;
  }
  .card--front .wordmark { font-size: 78px; color: var(--front-mark); }
  .card--back .wordmark {
    position: absolute; left: 40px; top: 36px;
    font-size: 72px; color: var(--brand-gray);
  }

  .divider {
    position: absolute; left: 40px; right: 30px; top: 196px;
    height: 1px; background: var(--brand-blue);
  }
  .person { position: absolute; left: 40px; top: 158px; }
  .person__name { font-weight: 700; font-size: 26px; color: var(--brand-blue); }
  .person__role {
    position: absolute; left: 40px; top: 204px;
    font-size: 15px; color: var(--ink);
  }
  .address {
    position: absolute; right: 30px; top: 140px;
    text-align: right; font-size: 15px; line-height: 1.3; color: var(--ink);
  }
  .contacts {
    position: absolute; left: 40px; top: 236px;
    list-style: none; font-size: 16px; color: var(--ink);
  }
  .contacts li { display: flex; align-items: center; gap: 12px; height: 28px; }
  .contacts svg { width: 16px; height: 16px; fill: var(--brand-blue); flex: none; }
</style>
</head>
<body>
  <section class="card card--front" aria-label="Card front">
    <span class="wordmark">veltrano</span>
  </section>

  <section class="card card--back" aria-label="Card back">
    <span class="wordmark">veltrano</span>
    <div class="person"><p class="person__name">Jonas Keller</p></div>
    <address class="address">Lindenweg 14b<br>10115 Berlin, Germany</address>
    <div class="divider"></div>
    <p class="person__role">CEO</p>
    <ul class="contacts">
      <li>
        <svg viewBox="0 0 16 16" aria-hidden="true"><path d="M2 5c0-2 2-3 6-3s6 1 6 3v1h-3V5H5v1H2zM4 7h8l2 6H2z"/></svg>
        +49 170 5550142
      </li>
      <li>
        <svg viewBox="0 0 16 16" aria-hidden="true"><path d="M1 3h14v10H1zM2 4l6 5 6-5z" fill-rule="evenodd"/></svg>
        info@veltrano.com
      </li>
      <li>
        <svg viewBox="0 0 16 16" aria-hidden="true"><circle cx="8" cy="8" r="7"/></svg>
        www.veltrano.com
      </li>
    </ul>
  </section>
</body>
</html>
```